Business Card Design Project

Bold, modern, clean business card design needed. Prefer double sided with art logo on the back. Front of card with company name logo, no art.

Target Market(s)

Our consulting company supports local, state and federal law enforcement officers. Therefore the design should be clean and direct with no flash or arrogance to it.

Industry/Entity Type

Business

```html
<!DOCTYPE html>
<html lang="en">
<head>
<meta charset="utf-8">
<title>Halvard Systems — Business Card</title>
<link href="https://fonts.googleapis.com/css2?family=Open+Sans:wght@400;600;700&display=swap" rel="stylesheet">
<style>
  :root {
    --backdrop: #221f1e;
    --card-black: #161616;
    --card-white: #ffffff;
    --ink: #111111;
    --accent: #8dc63f;
    --muted-grey: #3a3a3a;
  }
  * { box-sizing: border-box; margin: 0; padding: 0; }
  html, body {
    width: 1200px; height: 716px; overflow: hidden;
    background: var(--backdrop);
    font-family: "Open Sans", Arial, sans-serif;
  }
  .canvas {
    position: relative; width: 1200px; height: 716px;
    display: flex; align-items: center; justify-content: center; gap: 60px;
  }
  .card {
    position: relative; width: 500px; height: 286px; overflow: hidden;
    box-shadow: 0 10px 30px rgba(0,0,0,.5);
  }
  /* Back side */
  .card--back {
    background: var(--card-black);
    display: flex; align-items: center; justify-content: center; gap: 14px;
  }
  .back-mark {
    width: 18px; height: 18px; border-radius: 50%;
    background: var(--muted-grey);
  }
  .back-name {
    color: var(--muted-grey); font-weight: 700; font-size: 30px;
    letter-spacing: 3px; text-transform: uppercase;
  }
  /* Front side */
  .card--front { background: var(--card-white); }
  .front-company {
    position: absolute; left: 34px; top: 30px;
    color: var(--ink); font-weight: 700; font-size: 34px;
    letter-spacing: 4px; text-transform: uppercase; line-height: 1;
  }
  .front-person { position: absolute; left: 34px; top: 98px; }
  .person-name {
    color: var(--accent); font-weight: 700; font-size: 17px;
    text-transform: uppercase; letter-spacing: .3px;
  }
  .person-title {
    color: var(--ink); font-size: 10px; text-transform: uppercase; margin-top: 1px;
  }
  .contact-list { list-style: none; position: absolute; left: 34px; top: 152px; }
  .contact-item {
    display: flex; align-items: center; gap: 8px;
    color: var(--ink); font-size: 13px; line-height: 22px;
  }
  .contact-icon { width: 12px; height: 12px; flex: none; }
  .side-panel {
    position: absolute; right: 0; top: 70px; width: 150px; height: 216px;
    background: var(--ink);
  }
  .address-strip {
    position: absolute; left: 0; right: 0; bottom: 0; height: 26px;
    background: var(--ink);
    color: var(--accent); font-weight: 700; font-size: 11.5px;
    text-transform: uppercase; line-height: 26px; padding-left: 16px;
  }
</style>
</head>
<body>
<main class="canvas">
  <section class="card card--back" aria-label="Card back">
    <span class="back-mark"></span>
    <span class="back-name">Halvard Systems</span>
  </section>

  <section class="card card--front" aria-label="Card front">
    <h1 class="front-company">Halvard Systems</h1>
    <div class="front-person">
      <p class="person-name">Martin R. Okafor</p>
      <p class="person-title">Manager</p>
    </div>
    <ul class="contact-list">
      <li class="contact-item">
        <svg class="contact-icon" viewBox="0 0 12 12"><rect width="12" height="12" rx="2" fill="var(--accent)"/><rect x="4" y="2" width="4" height="8" rx="1" fill="#fff"/></svg>
        240-555-0148
      </li>
      <li class="contact-item">
        <svg class="contact-icon" viewBox="0 0 12 12"><rect width="12" height="12" rx="2" fill="var(--accent)"/><rect x="2.5" y="3.5" width="7" height="5" fill="#fff"/><path d="M2.5 3.5 6 6.5 9.5 3.5" stroke="var(--accent)" fill="none"/></svg>
        martin@halvardsystems.com
      </li>
      <li class="contact-item">
        <svg class="contact-icon" viewBox="0 0 12 12"><rect width="12" height="12" rx="2" fill="var(--accent)"/><circle cx="6" cy="6" r="3.5" stroke="#fff" fill="none"/><path d="M2.5 6h7M6 2.5v7" stroke="#fff"/></svg>
        www.halvardsystems.com
      </li>
    </ul>
    <div class="side-panel" role="img" aria-label="Decorative area for the company emblem"></div>
    <p class="address-strip">2290 Harbor Ln, Suite C4 Glenwood MD 20999</p>
  </section>
</main>
</body>
</html>
```